Business Card for a New Zealand IT Startup

I need a business card for Talmor Ventures. We are a young startup based in New Zealand working in internet marketing and web development. The design should have some element connected to New Zealand, such as wave, koru or silver fern, just don't use a kiwi bird.

```html
<!DOCTYPE html>
<html lang="en">
<head>
<meta charset="utf-8">
<title>Talmor Ventures — Business Card</title>
<link href="https://fonts.googleapis.com/css2?family=Montserrat:wght@600;700&family=Questrial&display=swap" rel="stylesheet">
<style>
  :root{
    --stage:#1c1c1c;
    --card-dark:#1f1f20;
    --card-light:#ffffff;
    --brand-blue:#1670bf;
    --brand-orange:#f2642a;
    --ink:#2b2b2b;
    --divider:#3a3a3a;
  }
  *{margin:0;padding:0;box-sizing:border-box}
  html,body{width:1200px;height:895px;overflow:hidden}
  body{
    background:var(--stage);
    display:flex;flex-direction:column;align-items:center;justify-content:center;gap:40px;
    font-family:"Questrial",sans-serif;
  }
  .card{width:620px;height:354px;position:relative;overflow:hidden;box-shadow:0 12px 30px rgba(0,0,0,.55)}
  .card--front{background:var(--card-dark)}
  .card--back{background:var(--card-light)}

  .wordmark{
    font-family:"Montserrat",sans-serif;font-weight:700;color:var(--brand-blue);
    display:flex;align-items:center;gap:12px;letter-spacing:1px;
  }
  .wordmark__dot{width:16px;height:16px;border-radius:50%;background:var(--brand-blue)}
  .card--front .wordmark{position:absolute;left:0;right:0;top:112px;justify-content:center;font-size:40px}
  .front-band{position:absolute;left:0;right:0;bottom:0;height:34px;background:var(--brand-blue);border-top:4px solid var(--brand-orange)}

  .card--back .wordmark{position:absolute;left:40px;top:158px;font-size:28px}
  .contact{position:absolute;left:336px;top:62px;width:260px;color:var(--ink)}
  .contact__group{border-left:2px solid var(--divider);padding-left:14px;margin-bottom:18px}
  .contact__group--address{border-color:var(--brand-orange)}
  .contact__group--lines{border-color:var(--brand-blue)}
  .contact__name{font-family:"Montserrat",sans-serif;font-weight:700;color:var(--brand-blue);font-size:22px;letter-spacing:.5px;line-height:1.1}
  .contact__title{font-size:15px}
  .contact__text{font-size:14px;line-height:1.45}
  .contact__line{display:flex;align-items:center;gap:8px;font-size:14px;line-height:1.6}
  .contact__line svg{width:13px;height:13px;flex:none}
</style>
</head>
<body>
  <section class="card card--front" aria-label="Card front">
    <div class="wordmark"><span class="wordmark__dot"></span>Talmor Ventures</div>
    <div class="front-band"></div>
  </section>

  <section class="card card--back" aria-label="Card back">
    <div class="wordmark"><span class="wordmark__dot"></span>Talmor Ventures</div>
    <div class="contact">
      <div class="contact__group">
        <div class="contact__name">ARIA KINGSLEY</div>
        <div class="contact__title">Director</div>
      </div>
      <div class="contact__group contact__group--address">
        <div class="contact__text">48 Harbour Lane, Suite 3<br>New Zealand</div>
      </div>
      <div class="contact__group contact__group--lines">
        <div class="contact__line">
          <svg viewBox="0 0 24 24" fill="var(--brand-orange)"><path d="M6.6 10.8a15.1 15.1 0 0 0 6.6 6.6l2.2-2.2a1 1 0 0 1 1-.25 11.4 11.4 0 0 0 3.6.57 1 1 0 0 1 1 1V20a1 1 0 0 1-1 1A17 17 0 0 1 3 4a1 1 0 0 1 1-1h3.5a1 1 0 0 1 1 1c0 1.25.2 2.45.57 3.6a1 1 0 0 1-.25 1z"/></svg>
          021 555 0148
        </div>
        <div class="contact__line">
          <svg viewBox="0 0 24 24" fill="var(--brand-orange)"><path d="M2 5h20v14H2z" opacity=".9"/><path d="M2 5l10 8 10-8" fill="none" stroke="#fff" stroke-width="2"/></svg>
          aria@talmorventures.com
        </div>
        <div class="contact__line">
          <svg viewBox="0 0 24 24" fill="none" stroke="var(--brand-orange)" stroke-width="2"><circle cx="12" cy="12" r="10"/><path d="M2 12h20M12 2c3 3 3 17 0 20M12 2c-3 3-3 17 0 20"/></svg>
          www.talmorventures.com
        </div>
      </div>
    </div>
  </section>
</body>
</html>
```